Brochure for a civil enineering company in A4 format

I need a brochure design for our company TALVI Engineering S.r.l.. We are an engineering consultant company. Our main clients are from the infrastructure industry (geotechnical and underground sectors mainly).
We are looking for a 2 pages (4 faces) fold out design with a glued pocket where we can put individual data sheets.
I need A4 format pages.

Target Market(s)

We are an engineering consultant company. Our main clients are from the infrastructure industry (geotechnical and underground sectors mainly).

Industry/Entity Type

Civil Engineer

Font styles to use
Sans Serif

Requirements
Must have
• Overall: 2 pages in A4 format
Essential style. Bright and modern appearance.
Glued pocket
Logo integrated in a picture on the pocket where I would like to insert a slogan (… talvi engineering … reliable solutions …)
Attached are selected images which the designer can use and edit at their own discretion.
Some advice in the following (anyway designers are free to provide their solutions):
Outer sheets:
Front page with name, logo. It could be nice to have the “m” of the logo integrated in a pictures, also a modified picture (I mean modify one of the attached pictures) so to create a general image and do not tie the cover to a specific job.
Back page: offices address and contact email address. Nice to have one space for a slogan.
Inner sheet: text that I upload in the file “inside-sheets”, possibly with pictures on each sheet. In the right faces insert the glued pocket. On this pages insert the section OUR EXPERIENCE ….with a space for a picture of our team.
Nice to have
• Clean and essential design.
Pictures choosing from the atteched ones. Pictures could be modified in a very light manner to make them a general idea of the work ( I mean geotechnical world) without to be immediately linked to a specific site.
Should not have
• excessive frills

```html
<!DOCTYPE html>
<html lang="it">
<head>
<meta charset="utf-8">
<title>TALVI Engineering – Brochure</title>
<link href="https://fonts.googleapis.com/css2?family=Montserrat:wght@400;500;600;700&display=swap" rel="stylesheet">
<style>
:root{
  --backdrop:#4d4d4d;
  --paper:#f7f7f7;
  --paper-shade:#ececec;
  --ink:#2b2b2b;
  --ink-soft:#555;
  --rule:#3a3a3a;
  --hatch:#e2e2e2;
  --band:#1e1e1e;
}
*{margin:0;padding:0;box-sizing:border-box}
html,body{width:1148px;height:1200px;overflow:hidden;background:var(--backdrop);font-family:'Montserrat',sans-serif;color:var(--ink)}
.spread{position:absolute;left:78px;width:992px;height:467px;background:linear-gradient(135deg,#efefef 0%,var(--paper) 45%,#fff 100%);overflow:hidden}
.spread--outer{top:94px}
.spread--inner{top:640px;height:468px}
.fold{position:absolute;top:0;bottom:0;width:1px;background:rgba(0,0,0,.06)}
.abs{position:absolute}
.photo{position:absolute}
.hatch-box{position:absolute;background:var(--hatch)}
.heading{position:absolute;font-size:13.5px;font-weight:400;letter-spacing:.3px;white-space:nowrap}
.heading b{font-weight:600}
.rule{position:absolute;height:1px;background:var(--rule)}
.body{position:absolute;font-size:5.6px;line-height:1.4;color:var(--ink-soft);text-align:justify}
.body p{margin-bottom:5px}
.body--tight{font-size:4.9px;line-height:1.38}
.body strong{color:var(--ink);font-weight:600}
.wordmark{position:absolute;font-weight:600;color:var(--ink);letter-spacing:1px;line-height:1}
.offices{position:absolute;left:364px;top:297px;font-size:7px;line-height:1.35;color:var(--ink)}
.offices .firm{font-weight:700;font-size:7.6px;margin-bottom:10px}
.office{padding-left:11px;margin-bottom:10px}
.office .line{position:relative}
.office svg{position:absolute;left:-11px;top:1px;width:6px;height:6px}
.slogan{position:absolute;left:690px;top:408px;width:272px;text-align:center;font-size:11px;font-weight:600;letter-spacing:.4px;color:var(--ink)}
.founders-band{position:absolute;left:694px;top:95px;width:143px;height:13px;background:var(--band);clip-path:polygon(0 0,92% 0,100% 100%,0 100%);color:#fff;font-size:8px;font-weight:500;padding:2px 0 0 9px;letter-spacing:.3px}
</style>
</head>
<body>

<!-- Outer sheet -->
<section class="spread spread--outer">
  <div class="fold" style="left:330px"></div>
  <div class="fold" style="left:661px"></div>

  <!-- Our company -->
  <h2 class="heading" style="left:34px;top:34px">OUR <b>COMPANY</b></h2>
  <div class="rule" style="left:34px;top:54px;width:262px"></div>
  <div class="body" style="left:34px;top:66px;width:262px">
    <p>TALVI Engineering S.r.l. offre servizi di consulenza tecnica, contrattuale e strategica ai principali attori nei settori delle scienze geologiche, dell'ingegneria geotecnica e dell'ingegneria idraulica. Lavoriamo per mitigare il rischio e ridurre l'incertezza, con flessibilità nella ricerca della soluzione ottimale contribuendo ad aumentare la redditività del progetto.</p>
    <p>TALVI Engineering S.r.l. è una società indipendente che nasce nel luglio 2020 dall'associazione di un gruppo di professionisti che hanno messo a fattor comune la reciproca esperienza maturata in oltre trent'anni di attività come progettisti e consulenti nel settore delle grandi opere di ingegneria civile lavorando come Direttori Tecnici di Main Engineering Companies and as Freelancers.</p>
    <p>TALVI Engineering S.r.l. vuole unire l'esperienza dei Fondatori e delle figure chiave con l'entusiasmo di chi intraprende una nuova attività, per dare vita ad una nuova realtà che si pone come obbiettivo principale il design of infrastructures that are safe, sustainable and economic.</p>
    <p>Each of our projects represents a long term commitment, we believe in providing safe, reliable, sustainable and innovative solutions. This is and will be our distinctive characteristic.</p>
  </div>
  <div class="hatch-box" style="left:131px;top:282px;width:165px;height:164px"></div>
  <div class="photo" role="img" aria-label="Photo of a large excavation site with reinforcement works between buildings" style="left:34px;top:216px;width:191px;height:210px;background:linear-gradient(180deg,#9fb8cc 0%,#8a8378 30%,#b9b3a6 65%,#9c9890 100%)"></div>

  <!-- Our offices -->
  <div class="hatch-box" style="left:430px;top:36px;width:165px;height:166px"></div>
  <h2 class="heading" style="left:364px;top:272px">OUR <b>OFFICES</b></h2>
  <div class="rule" style="left:364px;top:290px;width:146px"></div>
  <div class="offices">
    <div class="firm">TALVI Engineering S.r.l.</div>
    <div class="office">
      <div class="line">Milano</div>
      <div class="line"><svg viewBox="0 0 10 10"><circle cx="5" cy="3.5" r="2.5" fill="none" stroke="#2b2b2b" stroke-width="1.2"/><path d="M5 6v4" stroke="#2b2b2b" stroke-width="1.2"/></svg>Via Lario, 14</div>
      <div class="line">20100 Milano - IT</div>
      <div class="line" style="margin-top:3px"><svg viewBox="0 0 10 10"><circle cx="5" cy="5" r="4.3" fill="none" stroke="#2b2b2b" stroke-width="1"/><path d="M3.3 3c.3 2 1.5 3.3 3.4 4" stroke="#2b2b2b" stroke-width="1.2" fill="none"/></svg>+39 02 555010000</div>
      <div class="line"><svg viewBox="0 0 10 10"><rect x=".5" y="2" width="9" height="6" fill="none" stroke="#2b2b2b" stroke-width="1"/><path d="M.5 2l4.5 3.5L9.5 2" stroke="#2b2b2b" stroke-width="1" fill="none"/></svg>info@talviengineering.org</div>
    </div>
    <div class="office">
      <div class="line">Arco TN</div>
      <div class="line"><svg viewBox="0 0 10 10"><circle cx="5" cy="3.5" r="2.5" fill="none" stroke="#2b2b2b" stroke-width="1.2"/><path d="M5 6v4" stroke="#2b2b2b" stroke-width="1.2"/></svg>Via dei Tigli, 9</div>
      <div class="line">38062 Arco TN - IT</div>
      <div class="line" style="margin-top:3px"><svg viewBox="0 0 10 10"><circle cx="5" cy="5" r="4.3" fill="none" stroke="#2b2b2b" stroke-width="1"/><path d="M3.3 3c.3 2 1.5 3.3 3.4 4" stroke="#2b2b2b" stroke-width="1.2" fill="none"/></svg>+39 02 555010000</div>
      <div class="line"><svg viewBox="0 0 10 10"><rect x=".5" y="2" width="9" height="6" fill="none" stroke="#2b2b2b" stroke-width="1"/><path d="M.5 2l4.5 3.5L9.5 2" stroke="#2b2b2b" stroke-width="1" fill="none"/></svg>info@talviengineering.org</div>
    </div>
    <div class="office">
      <div class="line"><svg viewBox="0 0 10 10"><circle cx="5" cy="5" r="4.2" fill="none" stroke="#2b2b2b" stroke-width="1"/><path d="M.8 5h8.4M5 .8c-2.4 2.6-2.4 5.8 0 8.4M5 .8c2.4 2.6 2.4 5.8 0 8.4" stroke="#2b2b2b" stroke-width=".8" fill="none"/></svg>www.talviengineering.org</div>
    </div>
  </div>
  <div class="wordmark" style="left:554px;top:420px;font-size:18px">talvi</div>

  <!-- Cover -->
  <div class="wordmark" style="left:775px;top:30px;font-size:36px">talvi</div>
  <div class="abs" style="left:549px;top:99px;width:441px;height:269px;background:#fff"></div>
  <div class="photo" role="img" aria-label="Photo of a tunnel excavation with twin arched vaults, toned blue" style="left:554px;top:102px;width:267px;height:262px;background:linear-gradient(180deg,#5a63a0 0%,#3b3f72 45%,#56587e 75%,#7b7c96 100%)"></div>
  <div class="photo" role="img" aria-label="Aerial photo of a construction yard with cranes and materials" style="left:826px;top:102px;width:160px;height:144px;background:linear-gradient(160deg,#9b9a95 0%,#7d7a72 50%,#a29a8c 100%)"></div>
  <div class="photo" role="img" aria-label="Aerial photo of a site camp among green vegetation" style="left:826px;top:251px;width:160px;height:113px;background:linear-gradient(160deg,#7a9265 0%,#aaaaa3 45%,#8e9c7a 100%)"></div>
  <div class="slogan">TALVI ENGINEERING, RELIABLE SOLUTIONS</div>
</section>

<!-- Inner sheet -->
<section class="spread spread--inner">
  <div class="fold" style="left:330px"></div>
  <div class="fold" style="left:661px"></div>

  <!-- Pocket flap with photos -->
  <div class="photo" role="img" aria-label="Photo of a crawler crane lifting a tunnel boring machine shield" style="left:25px;top:36px;width:145px;height:142px;background:linear-gradient(180deg,#3f8fd0 0%,#6aa7d8 45%,#8e8f94 100%)"></div>
  <div class="photo" role="img" aria-label="Photo of a terraced slope excavation on a wooded hillside" style="left:181px;top:36px;width:114px;height:142px;background:linear-gradient(180deg,#4f7a3a 0%,#6c8456 40%,#a59c8c 100%)"></div>
  <div class="photo" role="img" aria-label="Photo of twin tunnel portals cut into a hillside with a drilling rig" style="left:25px;top:189px;width:270px;height:142px;background:linear-gradient(180deg,#b9c7d4 0%,#7f7c70 40%,#5f5c55 75%,#8a8578 100%)"></div>
  <div class="photo" role="img" aria-label="Photo of an excavator working on a site with a sheet pile wall" style="left:0;top:353px;width:320px;height:115px;clip-path:polygon(0 0,290px 0,320px 100%,0 100%);background:linear-gradient(180deg,#b7c3cc 0%,#7a7768 40%,#8c8878 100%)"></div>
  <div class="wordmark" style="left:48px;top:385px;font-size:46px;color:#222">talvi</div>

  <!-- Our services -->
  <h2 class="heading" style="left:364px;top:25px">OUR <b>SERVICES</b></h2>
  <div class="rule" style="left:364px;top:44px;width:262px"></div>
  <div class="body" style="left:364px;top:55px;width:262px">
    <p>Progettazione e consulenza specialistica nel campo della geologia, dell'ingegneria geotecnica, delle opere sotterranee e dell'ingegneria idraulica.</p>
    <p>Aiutiamo i nostri clienti a risolvere problemi di natura progettuale, contrattuale e costruttiva che possono nascere nell'intera vita del progetto portando la nostra esperienza all'interno delle loro organizzazioni, migliorando la qualità dei loro servizi di ingegneria, ottimizzando i loro progetti, proponendo nuove idee e soluzioni, rafforzando i loro approcci ......</p>
    <p>TALVI Engineering è in grado di fornire la propria assistenza nell'intero iter procedurale, dalla fase di indagine preliminare e di analisi di fattibilità fino alla progettazione costruttiva e all'assistenza tecnica in fase realizzativa.</p>
  </div>
  <div class="photo" role="img" aria-label="Photo of a tunnel face excavation with rock debris" style="left:364px;top:139px;width:262px;height:116px;background:radial-gradient(ellipse at 50% 55%,#8a7452 0%,#6b624f 45%,#8c8b80 100%)"></div>
  <div class="body" style="left:364px;top:266px;width:262px"><strong>La specializzazione e l'esperienza accumulate nelle discipline della geologia, dell'ingegneria geotecnica e del sottosuolo e dell'idraulica ci permette di massimizzare la nostra efficacia quando sia necessario:</strong></div>
  <div class="hatch-box" style="left:352px;top:337px;width:50px;height:46px"></div>
  <div class="photo" role="img" aria-label="Photo of a deep shaft excavation with a tunnel entrance" style="left:364px;top:295px;width:93px;height:76px;background:linear-gradient(180deg,#8a8880 0%,#6f6b62 50%,#9a9488 100%)"></div>
  <div class="body" style="left:477px;top:299px;width:149px">
    <p>far fronte a situazioni di emergenza anche su progetti in fase di sviluppo avanzato garantendo l'immediata focalizzazione delle problematiche di progetto e garantendo il risultato finale atteso (in termini di qualità, tempistiche e costi...)</p>
    <p>fornire "second opinion" di elevato valore tecnico ed amministrativo in occasione di problematiche progettuali e costruttive e dispute legali</p>
  </div>
  <div class="body" style="left:364px;top:391px;width:157px">
    <p>analizzare in tempi brevi progetti svolti da terzi individuandone le "criticità", verificandone la cantierabilità e la validità tecnico economica.</p>
    <p>ottimizzare i progetti redatti da terzi implementandone il contenuto e massimizzando l'efficacia economica degli investimenti.</p>
  </div>
  <div class="hatch-box" style="left:591px;top:412px;width:47px;height:46px"></div>
  <div class="photo" role="img" aria-label="Photo of a building foundation construction site" style="left:533px;top:373px;width:93px;height:76px;background:linear-gradient(180deg,#b0aba2 0%,#8c857a 50%,#a09789 100%)"></div>

  <!-- Our expertise -->
  <h2 class="heading" style="left:694px;top:25px">OUR <b>EXPERTISE AND EXPERIENCE</b></h2>
  <div class="rule" style="left:694px;top:44px;width:263px"></div>
  <div class="body" style="left:694px;top:58px;width:263px">
    <p>La società nasce dall'associazione di un gruppo di professionisti, con indiscusse competenze ed affidabilità, con esperienza maturata in oltre trent'anni di attività come progettisti e consulenti nel settore delle grandi opere di ingegneria civile; geologia, ingegneria geotecnica ed idraulica e opere sotterranee sono il "core" delle loro competenze ....</p>
  </div>
  <div class="founders-band">I SOCI FONDATORI SONO:</div>
  <div class="rule" style="left:694px;top:107px;width:263px"></div>
  <div class="body body--tight" style="left:694px;top:116px;width:263px">
    <p>Luca. Già Direttore Tecnico e Socio di SRTV Srl, nel periodo di sua permanenza fino al dicembre 2018, ha per essa firmato tutti i progetti nel campo delle opere sotterranee e la maggior parte di quelli di ingegneria geotecnica. Da gennaio 2019 è Direttore Tecnico di ALTG. Può vantare più di 150 gallerie naturali, e numerosi progetti ed assistenze tecniche nel campo delle strutture geotecniche, delle sistemazioni idrogeologiche e dei versanti e delle opere di protezione ambientale. Negli ultimi dieci anni è stato responsabile di attività di assistenza tecnica, per imprese di costruzione, di opere il cui valore supera i 440 Mio EUR e di servizi di progettazione definitiva e/o esecutiva per opere il cui valore supera i 1.400 Mio EUR. Ha svolto attività di verifica e validazione, in Italia ed all'estero, di numerosi progetti il cui valore complessivo supera i 3.400 Mio EUR.</p>
  </div>
  <div class="photo" role="img" aria-label="Group photo of the company team" style="left:697px;top:180px;width:260px;height:100px;background:linear-gradient(180deg,#e8e6e2 0%,#c7b8a8 45%,#7f8fa6 100%)"></div>
  <div class="body body--tight" style="left:694px;top:291px;width:263px">
    <p>Paolo 30 anni di esperienza professionale. Coinvolto in più di 150 gallerie naturali con lunghezza complessiva superiore a 360 km. Numerosi progetti ed attività di assistenza tecnica nel campo delle strutture, delle sistemazioni idrogeologiche e dei versanti e delle opere di protezione ambientale. Negli ultimi dieci anni responsabile di attività di assistenza tecnica in corso d'opera, per imprese di costruzione, di opere il cui valore supera i 440 Mio EUR e di servizi di progettazione definitiva o esecutiva per opere il cui valore supera i 1.400 Mio EUR. Ha svolto attività di verifica ai fini della validazione, in Italia ed all'estero, di numerosi progetti il cui valore complessivo supera i 3.400 Mio EUR.</p>
  </div>
  <div class="body body--tight" style="left:694px;top:345px;width:263px">
    <p>Sara 30 anni di esperienza professionale. Coinvolta in più di 150 gallerie naturali con lunghezza complessiva superiore a 360 km. Numerosi progetti ed attività di assistenza tecnica nel campo delle strutture, delle sistemazioni idrogeologiche e dei versanti e delle opere di protezione ambientale. Negli ultimi dieci anni responsabile di attività di assistenza tecnica in corso d'opera, per imprese di costruzione, di opere il cui valore supera i 440 Mio EUR e di servizi di progettazione definitiva o esecutiva per opere il cui valore supera i 1.400 Mio EUR. Ha svolto attività di verifica ai fini della validazione, in Italia ed all'estero, di numerosi progetti il cui valore complessivo supera i 3.400 Mio EUR.</p>
  </div>
  <div class="body body--tight" style="left:694px;top:399px;width:263px">
    <p>Elena 30 anni di esperienza professionale. Coinvolta in più di 150 gallerie naturali con lunghezza complessiva superiore a 360 km. Numerosi progetti ed attività di assistenza tecnica nel campo delle strutture, delle sistemazioni idrogeologiche e dei versanti e delle opere di protezione ambientale. Negli ultimi dieci anni responsabile di attività di assistenza tecnica in corso d'opera, per imprese di costruzione, di opere il cui valore supera i 440 Mio EUR e di servizi di progettazione definitiva o esecutiva per opere il cui valore supera i 1.400 Mio EUR. Ha svolto attività di verifica ai fini della validazione, in Italia ed all'estero, di numerosi progetti il cui valore complessivo supera i 3.400 Mio EUR.</p>
  </div>
</section>

</body>
</html>
```